4"x6" Postcards Grand opening promotion for Med Spa

Put our logo on the forehead of mask. Not all photos of mask needed. Just what you think is necessary. Some ideas of what to write is below

🌟 GRAND OPENING SPECIAL 🌟
Celebrate with Lumora Medical Aesthetics!

We’re officially open in Maple Terrace, and to celebrate, we’re giving new clients a FREE Red-Light Therapy Mask β€” a $247 value!

✨ NEW CLIENT EXCLUSIVE
Get your skin glowing with this luxurious Red-Light Therapy Mask, yours FREE with select purchases or membership sign-ups β€”
a $247 gift, absolutely on us!

βœ” Boosts collagen production
βœ” Reduces redness & inflammation
βœ” Enhances skin tone and texture
βœ” Non-invasive, relaxing & easy to use

πŸ“ Visit us at:
Studio Vantra – Suites 14 & 15
4817 Cedar Vale Rd #340, Fairmont, TX 75291

πŸ•’ Hours:
Thursday & Friday: 10 AM – 5 PM
Saturday: 10:30 AM – 2 PM

πŸ“ž Spots are limited – don’t miss out on your $247 gift!
Call 469-318-4096 to schedule your appointment.

🌐 https://lumoramedicalaesthetics.example | @lumoramedicalaesthetics

Limited-time offer. While supplies last. Free mask available with specific purchases or membership sign-ups only.

```html
<!DOCTYPE html>
<html lang="en">
<head>
<meta charset="utf-8">
<title>Lumora Medical Aesthetics – Grand Opening Special</title>
<link rel="stylesheet" href="https://fonts.googleapis.com/css2?family=Roboto+Condensed:wght@700&family=Great+Vibes&family=Pinyon+Script&family=Poppins:wght@400&family=Cormorant+Garamond:ital,wght@1,500&family=Carlito:wght@400;700&family=Cinzel:wght@400&display=swap">
<style>
  :root {
    --backdrop: #adadad;
    --ink: #000000;
    --paper: #ffffff;
    --gold: #a38c4f;
    --text-dark: #1a1a1a;
    --glow-red: #f0544f;
    --glow-pink: #f7c2bd;
  }
  * { margin: 0; padding: 0; box-sizing: border-box; }
  html, body { width: 909px; height: 1200px; overflow: hidden; }
  body { background: var(--backdrop); position: relative; font-family: "Carlito", "Calibri", sans-serif; }

  .postcard {
    position: absolute; left: 122px; top: 101px;
    width: 664px; height: 996px;
    background: var(--ink); color: var(--paper); overflow: hidden;
  }
  .postcard > * { position: absolute; }

  .brand-name {
    top: 30px; left: 0; width: 100%; text-align: center;
    font-family: "Cinzel", serif; font-size: 17px; letter-spacing: 6px;
    color: var(--paper); line-height: 1.5;
  }

  .headline-grand {
    top: 82px; left: 0; width: 100%; text-align: center;
    font-family: "Roboto Condensed", sans-serif; font-weight: 700;
    font-size: 118px; line-height: 1; letter-spacing: -4px; color: var(--gold);
  }
  .headline-script {
    top: 132px; left: 0; width: 100%; text-align: center;
    font-family: "Great Vibes", cursive; font-size: 98px; line-height: 1.1;
    color: var(--paper); white-space: nowrap;
  }

  .tagline {
    top: 232px; left: 0; width: 100%; text-align: center;
    font-family: "Poppins", sans-serif; font-size: 17px;
  }
  .intro {
    top: 266px; left: 0; width: 664px; text-align: center; white-space: nowrap;
    font-family: "Cormorant Garamond", serif; font-style: italic; font-weight: 500;
    font-size: 20px; line-height: 28px;
  }

  .wave { left: 0; top: 0; width: 664px; height: 996px; }

  .product-visual {
    left: 0; top: 360px; width: 320px; height: 330px;
    background:
      radial-gradient(ellipse 38% 42% at 68% 48%, rgba(35,35,35,.8), rgba(35,35,35,0) 75%),
      radial-gradient(ellipse 65% 60% at 30% 55%, rgba(240,84,79,.75), rgba(247,194,189,.5) 50%, rgba(255,255,255,0) 80%);
  }

  .offer-title {
    top: 406px; left: 326px;
    font-family: "Pinyon Script", cursive; font-size: 41px; color: var(--ink); white-space: nowrap;
  }
  .offer-copy {
    top: 466px; left: 326px; width: 330px; white-space: nowrap;
    font-size: 16.5px; line-height: 23px; letter-spacing: .4px; color: var(--text-dark);
  }
  .benefits { top: 576px; left: 357px; list-style: none; color: var(--text-dark); font-size: 16.5px; letter-spacing: .3px; }
  .benefits li { display: flex; align-items: center; height: 31px; }
  .benefits svg { width: 19px; height: 19px; margin-right: 14px; flex: none; }

  .info-label { color: var(--gold); font-weight: 700; font-size: 17px; line-height: 20px; }
  .info-text { font-size: 15px; line-height: 20.5px; }
  .info-icon { width: 25px; height: 25px; }
  .visit { top: 776px; left: 85px; width: 245px; }
  .hours { top: 776px; left: 418px; width: 240px; }
  .visit-icon { top: 777px; left: 46px; }
  .hours-icon { top: 777px; left: 379px; }
  .info-divider { top: 775px; left: 348px; width: 1px; height: 75px; background: var(--gold); }

  .cta-box {
    top: 868px; left: 10px; width: 640px; height: 80px;
    border: 1.2px solid var(--gold); border-radius: 38px;
  }
  .cta-divider { top: 868px; left: 345px; width: 1.2px; height: 80px; background: var(--gold); }
  .cta-call {
    top: 876px; left: 20px; width: 320px; text-align: center; white-space: nowrap;
    font-size: 16.5px; line-height: 21px; letter-spacing: .3px;
  }
  .cta-links { top: 880px; left: 365px; font-size: 15.5px; line-height: 30px; }

  .fine-print {
    top: 962px; left: 0; width: 100%; text-align: center; font-size: 13.4px; white-space: nowrap;
  }
</style>
</head>
<body>
  <main class="postcard">
    <div class="brand-name">LUMORA MEDICAL AESTHETICS</div>

    <h1 class="headline-grand">GRAND</h1>
    <div class="headline-script">Opening Special</div>

    <p class="tagline">Celebrate with Lumora Medical Aesthetics!</p>
    <p class="intro">We’re officially open in Maple Terrace, and to celebrate, we’re giving new clients<br>a FREE Red-Light Therapy Mask – a $247 value!</p>

    <svg class="wave" viewBox="0 0 664 996" aria-hidden="true">
      <path fill="#ffffff" d="M0 360 C60 335 150 320 260 340 C380 362 480 400 580 388 C630 382 655 368 664 360 L664 729 C640 748 600 760 541 759 C430 755 300 700 180 698 C90 697 30 712 0 729 Z"/>
    </svg>

    <div class="product-visual" role="img" aria-label="Woman's profile facing a black LED red-light therapy mask glowing red"></div>

    <h2 class="offer-title">New Client Exclusive</h2>
    <p class="offer-copy">Get your skin glowing with this luxurious<br>Red-Light Therapy Mask, yours FREE with<br>select purchases or membership sign-ups<br>— a $247 gift, absolutely on us!</p>

    <ul class="benefits">
      <li><svg viewBox="0 0 20 20"><circle cx="10" cy="10" r="9" fill="none" stroke="#a38c4f" stroke-width="1"/><path d="M10 5 L15 10 L10 15 L5 10 Z" fill="none" stroke="#a38c4f" stroke-width="1"/></svg>Boosts collagen production</li>
      <li><svg viewBox="0 0 20 20"><circle cx="10" cy="10" r="9" fill="none" stroke="#a38c4f" stroke-width="1"/><path d="M10 5 L15 10 L10 15 L5 10 Z" fill="none" stroke="#a38c4f" stroke-width="1"/></svg>Enhances skin tone and texture</li>
      <li><svg viewBox="0 0 20 20"><circle cx="10" cy="10" r="9" fill="none" stroke="#a38c4f" stroke-width="1"/><path d="M10 5 L15 10 L10 15 L5 10 Z" fill="none" stroke="#a38c4f" stroke-width="1"/></svg>Reduces redness &amp; inflammation</li>
      <li><svg viewBox="0 0 20 20"><circle cx="10" cy="10" r="9" fill="none" stroke="#a38c4f" stroke-width="1"/><path d="M10 5 L15 10 L10 15 L5 10 Z" fill="none" stroke="#a38c4f" stroke-width="1"/></svg>Non-invasive, relaxing &amp; easy to use</li>
    </ul>

    <svg class="info-icon visit-icon" viewBox="0 0 24 24" aria-hidden="true">
      <circle cx="12" cy="12" r="12" fill="#a38c4f"/>
      <path d="M12 5.5a4.3 4.3 0 0 0-4.3 4.3c0 3.2 4.3 8 4.3 8s4.3-4.8 4.3-8A4.3 4.3 0 0 0 12 5.5z" fill="#000"/>
      <circle cx="12" cy="9.8" r="1.6" fill="#a38c4f"/>
    </svg>
    <div class="visit">
      <div class="info-label">VISIT US AT</div>
      <div class="info-text">Studio Vantra – Suites 14 &amp; 15<br>4817 Cedar Vale Rd #340, Fairmont, TX<br>75291</div>
    </div>

    <div class="info-divider"></div>

    <svg class="info-icon hours-icon" viewBox="0 0 24 24" aria-hidden="true">
      <circle cx="12" cy="12" r="12" fill="#a38c4f"/>
      <rect x="7" y="7.5" width="10" height="9" rx="1" fill="none" stroke="#000" stroke-width="1.2"/>
      <line x1="7" y1="10" x2="17" y2="10" stroke="#000" stroke-width="1.2"/>
      <circle cx="14.5" cy="14" r="1.6" fill="none" stroke="#000" stroke-width="1"/>
    </svg>
    <div class="hours">
      <div class="info-label">HOURS</div>
      <div class="info-text">Thursday &amp; Friday: 10 AM – 5 PM<br>Saturday: 10:30 AM – 2 PMTX</div>
    </div>

    <div class="cta-box"></div>
    <div class="cta-divider"></div>
    <p class="cta-call">Spots are limited – don’t miss out on<br>your $247 gift! Call 469-318-4096 to<br>schedule your appointment.</p>
    <div class="cta-links">https://lumoramedicalaesthetics.example<br>@lumoramedicalaesthetics</div>

    <p class="fine-print">Limited-time offer. While supplies last. Free mask available with specific purchases or membership sign-ups only.</p>
  </main>
</body>
</html>
```